Building Servicess

We need a new business card design for a company. We specialise in: Electrical/Site temporary electrics, Data/Network Installation, Passive Fire Protection

Industry/Entity Type

Construction

Contact Information for Business Card

Services provided as detailed on project description

Font styles to use
Serif

Colors
0054AA
0677BA
7BADD7
CADEEF
E8F1F8
00AB8E
00BBA5
67D7C9
C6EFE9
E9F9F6
EB3D1F
EC4F4E
F09395
F8D3D4
FCEDEE

Requirements
Must have
• Company logo-contact details-phone numbers

```html
<!DOCTYPE html>
<html lang="en">
<head>
<meta charset="utf-8">
<title>Brightline Services – Business Card</title>
<link href="https://fonts.googleapis.com/css2?family=Montserrat:wght@300;400;600;700&display=swap" rel="stylesheet">
<style>
  :root {
    --backdrop: #c9ced3;
    --card-grey: #5f6063;
    --panel-white: #f3f3f2;
    --brand-blue: #1a5ea8;
    --card-blue-top: #1667b6;
    --card-blue-bottom: #0a4c92;
    --divider: #9a9a9a;
    --contact-text: #7c7c7c;
    --name-text: #e2e2e2;
    --white: #ffffff;
  }
  * { margin: 0; padding: 0; box-sizing: border-box; }
  html, body {
    width: 1200px; height: 1200px; overflow: hidden;
    background: var(--backdrop);
    font-family: "Montserrat", Arial, sans-serif;
  }
  .canvas {
    position: relative; width: 1200px; height: 1200px;
    display: flex; flex-direction: column; align-items: center;
    justify-content: center; gap: 60px;
  }
  .card {
    position: relative; width: 840px; height: 480px;
    border-radius: 6px; overflow: hidden;
    box-shadow: 0 12px 30px rgba(0,0,0,0.18);
  }

  /* Front side */
  .card--front { background: var(--card-grey); }
  .front__panel {
    position: absolute; left: 0; top: 0;
    width: 770px; height: 300px;
    background: var(--panel-white);
  }
  .front__brand {
    position: absolute; left: 40px; top: 0; width: 320px; height: 300px;
    display: flex; align-items: center; justify-content: center; gap: 12px;
  }
  .brand-mark { width: 22px; height: 22px; background: var(--brand-blue); flex: none; }
  .brand-name {
    color: var(--brand-blue); font-weight: 700; font-size: 22px;
    line-height: 1.15; letter-spacing: 0.5px; text-transform: uppercase;
  }
  .front__divider {
    position: absolute; left: 390px; top: 40px;
    width: 1px; height: 220px; background: var(--divider);
  }
  .front__contacts {
    position: absolute; left: 420px; top: 70px;
    list-style: none; color: var(--contact-text);
    font-size: 17px; font-weight: 400;
  }
  .front__contacts li { display: flex; align-items: center; gap: 14px; margin-bottom: 16px; }
  .front__contacts svg { width: 18px; height: 18px; fill: var(--brand-blue); flex: none; }
  .front__person {
    position: absolute; left: 0; top: 300px; width: 770px; height: 180px;
    display: flex; flex-direction: column; align-items: center; justify-content: center;
    color: var(--name-text);
  }
  .person-name { font-size: 40px; letter-spacing: 1px; text-transform: uppercase; }
  .person-name__first { font-weight: 700; }
  .person-name__last { font-weight: 300; }
  .person-role { font-size: 20px; font-weight: 600; letter-spacing: 1.5px; margin-top: 4px; }

  /* Back side */
  .card--back {
    background: linear-gradient(160deg, var(--card-blue-top), var(--card-blue-bottom));
    display: flex; align-items: center; justify-content: center; gap: 22px;
  }
  .card--back .brand-mark { width: 40px; height: 40px; background: var(--white); }
  .card--back .brand-name { color: var(--white); font-size: 44px; font-weight: 600; }
</style>
</head>
<body>
<main class="canvas">
  <section class="card card--front">
    <div class="front__panel">
      <div class="front__brand">
        <span class="brand-mark"></span>
        <span class="brand-name">Brightline Services Ltd</span>
      </div>
      <div class="front__divider"></div>
      <ul class="front__contacts">
        <li>
          <svg viewBox="0 0 24 24" aria-hidden="true"><path d="M6.6 10.8a15.1 15.1 0 0 0 6.6 6.6l2.2-2.2a1 1 0 0 1 1-.25 11.4 11.4 0 0 0 3.6.57 1 1 0 0 1 1 1V20a1 1 0 0 1-1 1A17 17 0 0 1 3 4a1 1 0 0 1 1-1h3.5a1 1 0 0 1 1 1c0 1.25.2 2.45.57 3.57a1 1 0 0 1-.25 1z"/></svg>
          555-014-270
        </li>
        <li>
          <svg viewBox="0 0 24 24" aria-hidden="true"><path d="M2 5h20v14H2z M4 7v.5l8 5 8-5V7l-8 5z" fill-rule="evenodd"/></svg>
          info@brightlineservices.com
        </li>
      </ul>
    </div>
    <div class="front__person">
      <p class="person-name"><span class="person-name__first">Daniel</span><span class="person-name__last">Reed</span></p>
      <p class="person-role">OWNER</p>
    </div>
  </section>

  <section class="card card--back">
    <span class="brand-mark"></span>
    <span class="brand-name">Brightline<br>Services Ltd</span>
  </section>
</main>
</body>
</html>
```